ruCover Business Card Design Project

We need a business card design for ruCover. ruCover is an underwriting agency. Underwriting agencies act on behalf of insurers, to underwrite insurance. We will be operating in specialised classes of insurance initially and looking to expand from there. We would like to see designs that incorporate our logo colours as well as a contrasting stand out colour - also we'd like the logo itself to be embossed on the card.

Insurance

Requirements
Must have
• Logo on front
Nice to have
• Logo solely featured on back of card
Should not have
• Please do not use comic cans font :)

```html
<!DOCTYPE html>
<html lang="en">
<head>
<meta charset="utf-8">
<title>ruCover Business Card</title>
<link rel="stylesheet" href="https://fonts.googleapis.com/css2?family=Arimo:wght@400;700&display=swap">
<style>
  :root {
    --page-bg: #ffffff;
    --card-front: #f3f3f3;
    --ink-dark: #3a3a3a;
    --ink-mid: #555555;
    --brand-blue: #1f5fae;
    --back-light: #2f86d3;
    --back-deep: #0b5aad;
    --white: #ffffff;
    --card-shadow: rgba(0, 0, 0, 0.45);
  }
  html, body {
    margin: 0;
    padding: 0;
    width: 1200px;
    height: 900px;
    overflow: hidden;
    background: var(--page-bg);
    font-family: "Arimo", Arial, sans-serif;
  }
  .canvas {
    position: relative;
    width: 1200px;
    height: 900px;
  }
  .card {
    position: absolute;
    border-radius: 20px;
    box-shadow: 10px 10px 12px var(--card-shadow);
  }
  .card-front {
    left: 26px;
    top: 60px;
    width: 634px;
    height: 356px;
    background: var(--card-front);
  }
  .card-back {
    left: 532px;
    top: 452px;
    width: 636px;
    height: 356px;
    background: radial-gradient(ellipse at 48% 50%, var(--back-light) 0%, var(--back-deep) 60%, var(--back-deep) 100%);
  }
  .brand-lockup {
    position: absolute;
    left: 474px;
    top: 84px;
    width: 160px;
    display: flex;
    flex-direction: column;
    align-items: center;
  }
  .brand-dot {
    width: 54px;
    height: 54px;
    border-radius: 50%;
    background: var(--brand-blue);
    margin-bottom: 10px;
  }
  .brand-name {
    font-weight: 700;
    font-size: 26px;
    letter-spacing: -0.5px;
    color: var(--brand-blue);
    line-height: 1;
  }
  .contact-row {
    position: absolute;
    left: 0;
    top: 254px;
    height: 52px;
    width: 100%;
  }
  .person {
    position: absolute;
    right: 460px;
    top: 8px;
    text-align: right;
    color: var(--ink-dark);
  }
  .person-name {
    font-weight: 700;
    font-size: 19px;
    line-height: 22px;
  }
  .person-title {
    font-weight: 700;
    font-size: 12px;
    line-height: 16px;
    color: var(--ink-mid);
  }
  .divider {
    position: absolute;
    top: 0;
    width: 8px;
    height: 52px;
    background: var(--brand-blue);
  }
  .divider-one { left: 198px; }
  .divider-two { left: 370px; }
  .contact-block {
    position: absolute;
    top: 4px;
    font-weight: 700;
    font-size: 18px;
    line-height: 23px;
    color: var(--ink-dark);
  }
  .phones { left: 222px; }
  .web { left: 400px; }
  .back-mark {
    position: absolute;
    inset: 0;
    display: flex;
    flex-direction: column;
    align-items: center;
    justify-content: center;
  }
  .back-circle {
    width: 150px;
    height: 150px;
    border-radius: 50%;
    background: var(--white);
    margin-bottom: 22px;
  }
  .back-name {
    font-weight: 700;
    font-size: 36px;
    color: var(--white);
    letter-spacing: -0.5px;
    line-height: 1;
  }
</style>
</head>
<body>
  <main class="canvas">
    <section class="card card-front" aria-label="Card front">
      <div class="brand-lockup">
        <div class="brand-dot"></div>
        <div class="brand-name">ruCover</div>
      </div>
      <div class="contact-row">
        <div class="person">
          <div class="person-name">your name here</div>
          <div class="person-title">your tittle here</div>
        </div>
        <div class="divider divider-one"></div>
        <div class="contact-block phones">
          <div>000-000-0000</div>
          <div>111-111-1111</div>
        </div>
        <div class="divider divider-two"></div>
        <div class="contact-block web">
          <div>youremail@email.com</div>
          <div>www.yourweb.com</div>
        </div>
      </div>
    </section>

    <section class="card card-back" aria-label="Card back">
      <div class="back-mark">
        <div class="back-circle"></div>
        <div class="back-name">ruCover</div>
      </div>
    </section>
  </main>
</body>
</html>
```